Quillbrook Pharma Business Card

Quillbrook Pharma in the upper left hand corner with the following underneath

Validated ERP Software
Pharma | Medical Devices | Contract Manufacturing

phone (555) 482-7316 x184

fax (555) 937-0658

email dvoss@quillbrooksystems.example

web www.quillbrooksystems.example

Harlow Bay | Fenmere | Port Ellison

```html
<!DOCTYPE html>
<html lang="en">
<head>
<meta charset="utf-8">
<title>Quillbrook Pharma Business Card</title>
<link href="https://fonts.googleapis.com/css2?family=Montserrat:wght@400;700;800&display=swap" rel="stylesheet">
<style>
  :root {
    --page: #2b2b2d;
    --blue-light: #1a7fd4;
    --blue: #0a5bb8;
    --blue-deep: #07489a;
    --green: #8cc63f;
    --white: #ffffff;
    --paper: #f4f5f6;
    --grey: #8a8f96;
    --rule: #6fa8e6;
  }
  * { box-sizing: border-box; margin: 0; padding: 0; }
  html, body { width: 1200px; height: 900px; overflow: hidden; }
  body {
    background: var(--page);
    font-family: "Montserrat", sans-serif;
    display: flex; flex-direction: column; align-items: center; justify-content: center;
    gap: 36px;
  }
  .card {
    width: 700px; height: 400px; position: relative; overflow: hidden;
    box-shadow: 0 14px 30px rgba(0,0,0,.45);
  }

  /* Back side */
  .card-back {
    background: radial-gradient(ellipse at 65% 25%, var(--blue-light), var(--blue) 60%, var(--blue-deep));
  }
  .card-back .texture { position: absolute; inset: 0; }
  .card-back .brand {
    position: absolute; right: 60px; top: 70px;
    display: flex; align-items: center; gap: 12px;
    color: var(--white); font-weight: 800; font-size: 36px; letter-spacing: .5px; text-transform: uppercase;
    white-space: nowrap;
  }
  .brand-dot { width: 20px; height: 20px; border-radius: 50%; background: var(--green); flex: none; }

  /* Front side */
  .card-front { background: var(--paper); }
  .front-top { position: absolute; left: 0; top: 0; right: 0; height: 196px; }
  .front-brand {
    position: absolute; right: 40px; top: 48px;
    display: flex; align-items: center; gap: 12px;
    color: var(--blue); font-weight: 800; font-size: 32px; text-transform: uppercase; letter-spacing: .5px;
    white-space: nowrap;
  }
  .tagline { position: absolute; left: 40px; top: 110px; }
  .tagline .lead { color: var(--green); font-weight: 700; font-size: 19px; line-height: 1.05; }
  .tagline .product { color: var(--blue); font-weight: 700; font-size: 19px; line-height: 1.1; }
  .cities { position: absolute; left: 40px; top: 163px; color: var(--grey); font-weight: 400; font-size: 15px; white-space: nowrap; }
  .cities .sep { color: var(--green); margin: 0 8px; }

  .front-band {
    position: absolute; left: 0; right: 0; top: 196px; height: 148px;
    background: linear-gradient(90deg, var(--blue-light), var(--blue) 55%, var(--blue-deep));
  }
  .person { position: absolute; right: 40px; top: 18px; text-align: right; }
  .person .name { color: var(--green); font-weight: 700; font-size: 22px; letter-spacing: .5px; text-transform: uppercase; }
  .person .role { color: var(--white); font-weight: 400; font-size: 14px; margin-top: 2px; }
  .rules { position: absolute; right: 0; top: 84px; width: 240px; height: 50px; }
  .contacts { position: absolute; left: 40px; top: 20px; list-style: none; }
  .contacts li {
    display: flex; align-items: center; gap: 10px;
    color: var(--white); font-size: 14px; font-weight: 400; line-height: 26px; white-space: nowrap;
  }
  .contacts svg { width: 15px; height: 15px; flex: none; }

  .industries {
    position: absolute; left: 0; right: 0; bottom: 0; height: 56px;
    background: var(--green);
    display: flex; align-items: center; padding-left: 40px;
    color: var(--blue); font-weight: 700; font-size: 15px; letter-spacing: .5px; text-transform: uppercase;
    white-space: nowrap;
  }
  .industries .sep { color: var(--white); margin: 0 8px; }
</style>
</head>
<body>

  <section class="card card-back" aria-label="Card back">
    <div class="texture" role="img" aria-label="Faint embossed repeating brand pattern across the blue background"></div>
    <div class="brand"><span class="brand-dot"></span>Quillbrook Pharma</div>
  </section>

  <section class="card card-front" aria-label="Card front">
    <div class="front-top">
      <div class="front-brand"><span class="brand-dot"></span>Quillbrook Pharma</div>
      <div class="tagline">
        <div class="lead">VALIDATED</div>
        <div class="product">ERP SOFTWARE</div>
      </div>
      <div class="cities">Harlow Bay<span class="sep">|</span>Fenmere<span class="sep">|</span>Port Ellison</div>
    </div>

    <div class="front-band">
      <ul class="contacts">
        <li>
          <svg viewBox="0 0 16 16" aria-hidden="true"><path fill="#8cc63f" d="M3.6 1.2 6 3.6 4.6 5.6c.9 2 2.3 3.5 4.2 4.4l2-1.4 2.4 2.4-1.6 2.2C6.4 13 2.2 8.8 1.4 3z"/></svg>
          (555) 482-7316 x184
        </li>
        <li>
          <svg viewBox="0 0 16 16" aria-hidden="true"><rect x="4" y="1.5" width="8" height="5" fill="#8cc63f"/><rect x="1.5" y="6" width="13" height="6" rx="1" fill="#8cc63f"/><rect x="4" y="10" width="8" height="4.5" fill="#fff" stroke="#8cc63f"/></svg>
          (555) 937-0658
        </li>
        <li>
          <svg viewBox="0 0 16 16" aria-hidden="true"><rect x="1" y="3" width="14" height="10" fill="#8cc63f"/><path d="M1 3l7 6 7-6" fill="none" stroke="#0a5bb8" stroke-width="1.2"/></svg>
          dvoss@quillbrooksystems.example
        </li>
        <li>
          <svg viewBox="0 0 16 16" aria-hidden="true"><g fill="none" stroke="#8cc63f" stroke-width="1.3"><circle cx="8" cy="8" r="6.3"/><ellipse cx="8" cy="8" rx="2.8" ry="6.3"/><path d="M1.7 8h12.6M2.8 4.8h10.4M2.8 11.2h10.4"/></g></svg>
          www.quillbrooksystems.example
        </li>
      </ul>
      <div class="person">
        <div class="name">Jordan Pellow</div>
        <div class="role">General Manager</div>
      </div>
      <svg class="rules" viewBox="0 0 240 50" aria-hidden="true">
        <g stroke="#6fa8e6" stroke-width="1" opacity=".7">
          <line x1="60" y1="6" x2="240" y2="6"/>
          <line x1="30" y1="24" x2="240" y2="24"/>
          <line x1="0" y1="42" x2="240" y2="42"/>
        </g>
      </svg>
    </div>

    <div class="industries">Pharma<span class="sep">|</span>Medical Devices<span class="sep">|</span>Contract Manufacturing</div>
  </section>

</body>
</html>
```